Bref créative
KORVO FREIGHT
BUSINESS CARDS AND BROCHURE LAYOUT
Professional
Reed Quandt
Owner/Specialist
I want no address
korvofreight@nubramail.com
www.korvofreight-example.com
just the logo on the back

```html
<!DOCTYPE html>
<html lang="en">
<head>
<meta charset="utf-8">
<title>Korvo Freight Stationery</title>
<link href="https://fonts.googleapis.com/css2?family=Open+Sans:wght@400;600;700&display=swap" rel="stylesheet">
<style>
  :root {
    --red: #d0202e;
    --red-dark: #9e1620;
    --charcoal: #2b2b2b;
    --grey: #6d6d6d;
    --line: #c9c9c9;
    --paper: #ffffff;
    --stage: #e8e5e1;
    --black: #141414;
  }
  * { box-sizing: border-box; margin: 0; padding: 0; }
  html, body { width: 1200px; height: 734px; overflow: hidden; }
  body {
    background: var(--stage);
    font-family: "Open Sans", Arial, sans-serif;
    color: var(--charcoal);
    position: relative;
  }
  .sheet {
    position: absolute;
    background: var(--paper);
    box-shadow: 0 4px 14px rgba(0,0,0,.18);
    overflow: hidden;
  }
  .swoosh { position: absolute; left: 0; top: 0; width: 100%; display: block; }
  .brand { display: flex; align-items: center; gap: 6px; }
  .brand-mark { width: 14px; height: 14px; background: var(--red); flex: none; }
  .brand-name { font-weight: 700; color: var(--charcoal); letter-spacing: .3px; white-space: nowrap; }
  .tagline { font-size: 6px; color: var(--grey); margin-top: 2px; }

  /* Fax cover */
  .fax { left: 40px; top: 90px; width: 250px; height: 370px; padding: 44px 22px 20px; }
  .fax .brand-name { font-size: 14px; }
  .fax-fields { margin-top: 22px; font-size: 8px; color: var(--grey); }
  .fax-field { border-bottom: 1px solid var(--line); height: 17px; line-height: 17px; }
  .fax-checks { display: flex; gap: 10px; font-size: 7px; color: var(--grey); margin: 12px 0 10px; }
  .fax-checks span::before { content: ""; display: inline-block; width: 7px; height: 7px; border: 1px solid var(--grey); margin-right: 3px; vertical-align: -1px; }
  .fax-comments { font-size: 8px; color: var(--grey); }
  .fax-rule { border-bottom: 1px solid var(--line); height: 13px; }
  .fax-footer { position: absolute; left: 22px; right: 22px; bottom: 12px; font-size: 5.5px; color: var(--grey); display: flex; justify-content: space-between; }

  /* Letterhead */
  .letterhead { left: 320px; top: 50px; width: 300px; height: 424px; }
  .letterhead .brand { position: absolute; left: 26px; top: 62px; }
  .letterhead .brand-name { font-size: 17px; }
  .letterhead .tagline-wrap { position: absolute; left: 46px; top: 84px; }
  .letter-footer { position: absolute; left: 26px; right: 26px; bottom: 14px; display: flex; justify-content: space-between; font-size: 5.5px; color: var(--grey); border-top: 1px solid var(--line); padding-top: 5px; }

  /* Envelope */
  .envelope { left: 650px; top: 70px; width: 510px; height: 230px; }
  .envelope .brand { position: absolute; left: 24px; top: 72px; }
  .envelope .brand-name { font-size: 18px; }
  .envelope .tagline-wrap { position: absolute; left: 44px; top: 96px; }
  .envelope .return { position: absolute; left: 44px; top: 112px; font-size: 6px; color: var(--grey); line-height: 1.5; }

  /* Cards */
  .card { width: 160px; height: 92px; border-radius: 3px; }
  .card.front-white { left: 650px; top: 330px; }
  .card.front-black { left: 830px; top: 330px; background: var(--black); }
  .card.back-white { left: 650px; top: 450px; background: linear-gradient(#ffffff, #e4e4e4); }
  .card.back-red { left: 830px; top: 450px; background: var(--red); }
  .card.back-black { left: 1010px; top: 450px; background: var(--black); }
  .card-front .brand { position: absolute; left: 10px; top: 40px; }
  .card .brand-name { font-size: 11px; }
  .card .person { position: absolute; right: 8px; top: 4px; text-align: right; z-index: 2; line-height: 1.25; }
  .card .person-name { font-size: 8px; font-weight: 700; color: #fff; }
  .card .person-role { font-size: 5.5px; color: #fff; }
  .card .contact { position: absolute; left: 10px; bottom: 8px; font-size: 5px; line-height: 1.5; color: var(--grey); }
  .front-black .brand-name { color: #fff; }
  .front-black .contact { color: #bdbdbd; }
  .back-logo { position: absolute; left: 0; right: 0; top: 28px; display: flex; justify-content: center; }
  .back-logo .brand-name { font-size: 12px; }
  .back-red .brand-name, .back-black .brand-name { color: #fff; }
  .back-red .brand-mark { background: #fff; }
  .arc { position: absolute; left: 0; bottom: 16px; width: 100%; height: 20px; }
</style>
</head>
<body>

  <!-- Fax cover sheet -->
  <section class="sheet fax">
    <svg class="swoosh" viewBox="0 0 250 40" preserveAspectRatio="none" height="40">
      <path d="M0 0H250V16C170 34 80 22 0 36Z" fill="var(--red)"/>
      <path d="M0 36C80 22 170 34 250 16" fill="none" stroke="var(--charcoal)" stroke-width="2"/>
    </svg>
    <div class="brand"><span class="brand-mark"></span><span class="brand-name">KORVO FREIGHT</span></div>
    <div class="tagline">Reliable freight, every time</div>
    <div class="fax-fields">
      <div class="fax-field">To:</div>
      <div class="fax-field">Fax:</div>
      <div class="fax-field">Phone:</div>
      <div class="fax-field">Re:</div>
    </div>
    <div class="fax-checks"><span>Urgent</span><span>For Review</span><span>Please Comment</span></div>
    <div class="fax-comments">Comments:</div>
    <div class="fax-rule"></div><div class="fax-rule"></div><div class="fax-rule"></div>
    <div class="fax-rule"></div><div class="fax-rule"></div><div class="fax-rule"></div>
    <div class="fax-rule"></div><div class="fax-rule"></div>
    <div class="fax-footer"><span>555-014-2290</span><span>korvofreight@nubramail.com</span><span>www.korvofreight-example.com</span></div>
  </section>

  <!-- Letterhead -->
  <section class="sheet letterhead">
    <svg class="swoosh" viewBox="0 0 300 54" preserveAspectRatio="none" height="54">
      <path d="M0 0H300V22C210 46 100 30 0 50Z" fill="var(--red)"/>
      <path d="M0 50C100 30 210 46 300 22" fill="none" stroke="var(--charcoal)" stroke-width="3"/>
    </svg>
    <div class="brand"><span class="brand-mark"></span><span class="brand-name">KORVO FREIGHT</span></div>
    <div class="tagline-wrap"><div class="tagline">Reliable freight, every time</div></div>
    <div class="letter-footer"><span>555-014-2290</span><span>korvofreight@nubramail.com</span><span>www.korvofreight-example.com</span></div>
  </section>

  <!-- Envelope -->
  <section class="sheet envelope">
    <svg class="swoosh" viewBox="0 0 510 60" preserveAspectRatio="none" height="60">
      <path d="M0 0H510V20C350 52 170 30 0 56Z" fill="var(--red)"/>
      <path d="M0 56C170 30 350 52 510 20" fill="none" stroke="var(--charcoal)" stroke-width="3"/>
    </svg>
    <div class="brand"><span class="brand-mark"></span><span class="brand-name">KORVO FREIGHT</span></div>
    <div class="tagline-wrap"><div class="tagline">Reliable freight, every time</div></div>
    <div class="return">korvofreight@nubramail.com<br>www.korvofreight-example.com</div>
  </section>

  <!-- Business card front, white -->
  <section class="sheet card card-front front-white">
    <svg class="swoosh" viewBox="0 0 160 34" preserveAspectRatio="none" height="34">
      <path d="M0 0H160V30C110 24 60 16 0 12Z" fill="var(--red)"/>
      <path d="M0 12C60 16 110 24 160 30" fill="none" stroke="var(--charcoal)" stroke-width="1.5"/>
    </svg>
    <div class="person"><div class="person-name">Reed Quandt</div><div class="person-role">Owner/Specialist</div></div>
    <div class="brand"><span class="brand-mark"></span><span class="brand-name">KORVO FREIGHT</span></div>
    <div class="contact">555-014-2290<br>korvofreight@nubramail.com<br>www.korvofreight-example.com</div>
  </section>

  <!-- Business card front, black -->
  <section class="sheet card card-front front-black">
    <svg class="swoosh" viewBox="0 0 160 34" preserveAspectRatio="none" height="34">
      <path d="M0 0H160V30C110 24 60 16 0 12Z" fill="var(--red)"/>
      <path d="M0 12C60 16 110 24 160 30" fill="none" stroke="#8a8a8a" stroke-width="1.5"/>
    </svg>
    <div class="person"><div class="person-name">Reed Quandt</div><div class="person-role">Owner/Specialist</div></div>
    <div class="brand"><span class="brand-mark"></span><span class="brand-name">KORVO FREIGHT</span></div>
    <div class="contact">555-014-2290<br>korvofreight@nubramail.com<br>www.korvofreight-example.com</div>
  </section>

  <!-- Business card backs -->
  <section class="sheet card back-white">
    <div class="back-logo"><div class="brand"><span class="brand-mark"></span><span class="brand-name">KORVO FREIGHT</span></div></div>
    <svg class="arc" viewBox="0 0 160 20" preserveAspectRatio="none"><path d="M30 18C60 4 100 4 130 18" fill="none" stroke="var(--grey)" stroke-width="1.5"/></svg>
  </section>
  <section class="sheet card back-red">
    <div class="back-logo"><div class="brand"><span class="brand-mark"></span><span class="brand-name">KORVO FREIGHT</span></div></div>
    <svg class="arc" viewBox="0 0 160 20" preserveAspectRatio="none"><path d="M30 18C60 4 100 4 130 18" fill="none" stroke="#fff" stroke-width="1.5"/></svg>
  </section>
  <section class="sheet card back-black">
    <div class="back-logo"><div class="brand"><span class="brand-mark"></span><span class="brand-name">KORVO FREIGHT</span></div></div>
    <svg class="arc" viewBox="0 0 160 20" preserveAspectRatio="none"><path d="M30 18C60 4 100 4 130 18" fill="none" stroke="#fff" stroke-width="1.5"/></svg>
  </section>

</body>
</html>
```